A reimagined website for a cross-border tax firm

There are two aspects to this project for Brindlemoor Tax Advisory:
1) I need a logo update to accommodate increasing focus and specialization in my business. The byline under the name “Brindlemoor Tax Advisory” needs to change:
ORIGINAL: TAX SUPPORT FOR PUBLIC ACCOUNTING FIRMS
REVISED: CROSS-BORDER TAX SERVICES • U.S. & CANADA
2) I need a website “refresh” (see current website at www.levyhelpdesk.example) based on this logo – a new vision for a website with greater clarity, focus and organization. It should represent a re-envisioning of the current approach, and not the wholesale abandonment of the style represented there. I need it to be creative, compelling and attention grabbing, but still professional. This should, at a minimum, update any places where the old name/logo is used, but I want the redesign to go beyond this to something more intuitive. I need high quality separate PNG files of the various logo styles for use in various documents, but HTML coding would be a helpful but not necessary addition.

Target Market(s)

People in need of cross-border tax services - Canada and US

Coding

Number of Pages Required

Requirements
Must have
• Greater crispness, sharpness - higher resolution
• A more compelling, organized approach - make the wording and images more accessible to the website user (especially the staff bios, which have scroll bars now)
Nice to have
• Replacement of stock image with a true image of the Halifax skyline
Should not have
• Deviate from colour pattern represented in website logo of blue/orange
• Deviate from existing logo except for word replacement

```html
<!DOCTYPE html>
<html lang="en">
<head>
<meta charset="utf-8">
<title>Brindlemoor Tax Advisory</title>
<link href="https://fonts.googleapis.com/css2?family=Cinzel:wght@400;700&family=Open+Sans:wght@400;600&display=swap" rel="stylesheet">
<style>
:root{
  --backdrop:#151515;
  --orange:#e98a26;
  --orange-dark:#c9661a;
  --navy:#213f6b;
  --blue:#2a7ab5;
  --red:#e94f24;
  --white:#ffffff;
  --ink:#333333;
  --muted:#666666;
  --gold:#d9a45a;
}
*{box-sizing:border-box;margin:0;padding:0}
html,body{width:706px;height:1200px;overflow:hidden}
body{background:var(--backdrop);font-family:'Open Sans',sans-serif;position:relative}
.brand{position:absolute;top:22px;left:0;width:706px;display:flex;justify-content:center;align-items:center;gap:10px;color:var(--white);font-family:'Cinzel',serif}
.brand-square{width:30px;height:30px;background:var(--orange)}
.brand-name{font-size:21px;font-weight:700;letter-spacing:.5px;border-bottom:1px solid var(--white);padding-bottom:2px;line-height:1.1}
.brand-byline{font-size:9.5px;letter-spacing:2.4px;margin-top:4px}
.page{position:absolute;left:58px;top:82px;width:589px}
.nav{height:36px;background:linear-gradient(var(--orange),var(--orange-dark));display:flex;align-items:center}
.nav a{flex:1 1 auto;text-align:center;color:var(--white);text-decoration:none;font-family:'Cinzel',serif;font-size:8px;border-right:1px solid rgba(255,255,255,.45);line-height:26px}
.nav a:last-child{border-right:0}
.hero{height:271px;background:linear-gradient(#4f8fd6 0%,#a9cbee 45%,#b8ab94 70%,#53606a 100%)}
.section-title{font-family:'Cinzel',serif;font-weight:700;text-align:center}
.divider{display:flex;align-items:center;justify-content:center;gap:8px;margin:14px auto 0;width:470px}
.divider span{flex:1;height:1px}
.divider i{display:block;width:52px;height:9px;border-radius:50%}
.welcome{height:198px;background:var(--navy);padding-top:26px;color:var(--white);text-align:center}
.welcome .section-title{font-size:18px}
.welcome .divider span{background:var(--gold)}
.welcome .divider i{background:var(--gold)}
.welcome p{font-size:6.6px;line-height:14px;width:440px;margin:18px auto 0}
.btn{display:inline-block;margin-top:17px;border:1px solid var(--white);border-radius:12px;padding:5px 14px;font-family:'Cinzel',serif;font-size:7.5px;font-weight:700;color:var(--white)}
.how{height:286px;background:var(--blue);padding-top:32px;color:var(--white)}
.how .section-title{font-size:18px}
.how .divider span,.how .divider i{background:#d7e7f4}
.steps{position:relative;height:200px}
.step{position:absolute;top:42px;width:144px;height:144px;border-radius:50%;background:var(--white);overflow:hidden}
.step .art{position:absolute;left:37px;top:14px;width:70px;height:70px;border-radius:8px}
.step .base{position:absolute;left:0;bottom:0;width:100%;height:44px;text-align:center;padding-top:21px;font-family:'Cinzel',serif;font-size:8.5px;font-weight:700;color:var(--white)}
.step .num{position:absolute;left:60px;top:88px;width:24px;height:24px;border-radius:50%;background:var(--blue);border:2px solid var(--white);color:var(--white);font-family:'Cinzel',serif;font-size:9px;font-weight:700;text-align:center;line-height:20px}
.s1{left:15px}.s1 .base{background:var(--orange)}.s1 .art{background:linear-gradient(#5ab3b3,#e7a34b)}
.s2{left:222px}.s2 .base{background:var(--navy)}.s2 .art{background:linear-gradient(#e9eef3,#7d8a99)}
.s3{left:429px}.s3 .base{background:var(--red)}.s3 .art{background:linear-gradient(#f2c89e,#d7382b)}
.blog{height:227px;background:#f6f6f6;padding-top:30px}
.blog .section-title{font-size:18px;color:#2b2b2b}
.blog .divider span,.blog .divider i{background:var(--orange)}
.posts{display:flex;margin-top:28px;padding-left:17px}
.post{width:196px;display:flex;gap:10px}
.thumb{width:51px;height:46px;flex:none}
.t1{background:linear-gradient(#e8e4dc,#8c8a84)}
.t2{background:linear-gradient(#d9c7a8,#6b5a49)}
.t3{background:linear-gradient(#4fb5c8,#9fd3dc)}
.post h3{font-family:'Cinzel',serif;font-size:7.5px;font-weight:400;color:#444;line-height:12px}
.post p{font-size:7px;color:var(--muted);line-height:14.5px;margin-top:6px}
.meta{display:flex;align-items:center;gap:4px;font-size:7px;color:var(--muted);margin-top:8px}
.meta svg{flex:none}
.meta .gap{width:6px}
.footer{height:56px;background:linear-gradient(var(--orange),var(--orange-dark));text-align:center;line-height:56px;color:var(--white);font-family:'Cinzel',serif;font-size:7.5px}
</style>
</head>
<body>
<header class="brand">
  <div class="brand-square"></div>
  <div>
    <div class="brand-name">BRINDLEMOOR TAX ADVISORY</div>
    <div class="brand-byline">CROSS-BORDER TAX SERVICES • U.S. &amp; CANADA</div>
  </div>
</header>
<main class="page">
  <nav class="nav">
    <a>Home</a><a>Our Team</a><a>For Indiviuals</a><a>For Accounting Firms</a><a>Contact</a><a>Payment</a>
  </nav>
  <div class="hero" role="img" aria-label="City riverside skyline photograph with bridge and towers"></div>
  <section class="welcome">
    <h2 class="section-title">Welcome To Brindlemoor Advisory</h2>
    <div class="divider"><span></span><i role="img" aria-label="Ornamental flourish"></i><span></span></div>
    <p>Nullam placerat aliquet eros eget tristique. Cras quis dolor facilisis erat suscipit dignissim. Vestibulum ante ipsum primis in faucibus orci luctus et ultrices posuere cubilia Curae; Phasellus ut congue dui. Sed vestibulum fringilla enim, in varius ante tempor in. Sed vulputate sollicitudin mi. Donec tristique finibus diam, et blandit eros fringilla</p>
    <span class="btn">Read More</span>
  </section>
  <section class="how">
    <h2 class="section-title">How It works</h2>
    <div class="divider"><span></span><i role="img" aria-label="Ornamental flourish"></i><span></span></div>
    <div class="steps">
      <div class="step s1"><div class="art" role="img" aria-label="Audit illustration with charts and devices"></div><div class="base">Audit</div><div class="num">1</div></div>
      <div class="step s2"><div class="art" role="img" aria-label="Document with magnifying glass illustration"></div><div class="base">Analyse</div><div class="num">2</div></div>
      <div class="step s3"><div class="art" role="img" aria-label="Hand holding phone with payment illustration"></div><div class="base">Claim</div><div class="num">3</div></div>
    </div>
  </section>
  <section class="blog">
    <h2 class="section-title">Latest Blog</h2>
    <div class="divider"><span></span><i role="img" aria-label="Ornamental flourish"></i><span></span></div>
    <div class="posts">
      <article class="post"><div class="thumb t1" role="img" aria-label="Desk with calculator and glasses photo"></div><div><h3>Quisque sapien nisl, hendrerit quis arcu ac</h3><p>Nulla eu pulvinar urna, eget pharetra tortor. Duis a lacus pretium, convalliQuisque</p><div class="meta"><svg width="8" height="8" viewBox="0 0 8 8"><path d="M1 1h6v4H3L1 7z" fill="#e98a26"/></svg>43 Comments<span class="gap"></span><svg width="8" height="8" viewBox="0 0 8 8"><rect x="1" y="3" width="6" height="4" fill="#e98a26"/><rect x="3" y="1" width="2" height="3" fill="#e98a26"/></svg>65 Likes</div></div></article>
      <article class="post"><div class="thumb t2" role="img" aria-label="Team meeting photo"></div><div><h3>Quisque sapien nisl, hendrerit quis arcu ac</h3><p>Nulla eu pulvinar urna, eget pharetra tortor. Duis a lacus pretium, convalliQuisque</p><div class="meta"><svg width="8" height="8" viewBox="0 0 8 8"><path d="M1 1h6v4H3L1 7z" fill="#e98a26"/></svg>43 Comments<span class="gap"></span><svg width="8" height="8" viewBox="0 0 8 8"><rect x="1" y="3" width="6" height="4" fill="#e98a26"/><rect x="3" y="1" width="2" height="3" fill="#e98a26"/></svg>65 Likes</div></div></article>
      <article class="post"><div class="thumb t3" role="img" aria-label="Office portrait photo"></div><div><h3>Quisque sapien nisl, hendrerit quis arcu ac</h3><p>Nulla eu pulvinar urna, eget pharetra tortor. Duis a lacus pretium, convalliQuisque</p><div class="meta"><svg width="8" height="8" viewBox="0 0 8 8"><path d="M1 1h6v4H3L1 7z" fill="#e98a26"/></svg>43 Comments<span class="gap"></span><svg width="8" height="8" viewBox="0 0 8 8"><rect x="1" y="3" width="6" height="4" fill="#e98a26"/><rect x="3" y="1" width="2" height="3" fill="#e98a26"/></svg>65 Likes</div></div></article>
    </div>
  </section>
  <footer class="footer">Copyright © 2017 Brindlemoor Tax Advisory Inc.</footer>
</main>
</body>
</html>
```